Modern Business Card for Lanternfield 2018

Our company assumes the best about people. We are creating an online community of entrepreneurs and business leaders who struggle with marketing their business online.

This business card should POP! We recently got a new logo and are launching a new website next month, so our business cards should make a statement that feels:
-Fresh
-Smart
-Trustworthy
-Fun

Target Market(s)

small business owners, entrepreneurs

Industry/Entity Type

Digital Marketing

Contact Information for Business Card

Dimensions: 3.5" x 2"

Font styles to use
Sans Serif

Colors
f37122
ffffff

Requirements
Must have
• We need a business card with a modern, bold design. We will use one side of the card as a lead-generation offer, so text on one side will need to fit up to 140 characters. The business card should stick to our core colors (orange, black, and white).
Nice to have
• We think a vertical "portrait" design could be interesting.
Should not have
• Should not look like a traditional business card. The round icon should stand out from a distance.

```html
<!DOCTYPE html>
<html lang="en">
<head>
<meta charset="utf-8">
<title>Lanternfield Business Card</title>
<link rel="stylesheet" href="https://fonts.googleapis.com/css2?family=Lobster&family=Roboto:wght@400;500;700;900&display=swap">
<style>
  :root {
    --orange: #f26a28;
    --white: #f6f6f6;
    --ink: #111111;
    --rule: #555555;
    --backdrop: #6a4630;
  }
  * { margin: 0; padding: 0; box-sizing: border-box; }
  html, body { width: 1200px; height: 960px; overflow: hidden; }
  body {
    position: relative;
    background: var(--backdrop);
    font-family: "Roboto", Arial, sans-serif;
  }
  .card {
    position: absolute;
    width: 599px;
    height: 343px;
    border-radius: 18px;
    overflow: hidden;
    background: var(--white);
    box-shadow: 0 3px 6px rgba(0,0,0,0.35);
  }
  .card-front { left: 315px; top: 113px; }
  .card-back { left: 311px; top: 472px; width: 600px; }

  /* front */
  .front-mark {
    position: absolute; left: 0; right: 0; top: 28px;
    display: flex; flex-direction: column; align-items: center; gap: 10px;
  }
  .mark-circle {
    width: 110px; height: 110px; border-radius: 50%;
    background: var(--orange);
  }
  .mark-name {
    font-weight: 900; font-size: 26px; letter-spacing: 1px;
    color: var(--orange); text-transform: uppercase;
  }
  .front-rule {
    position: absolute; left: 0; right: 0; top: 194px; height: 6px;
    background: linear-gradient(var(--white) 0 1px, var(--rule) 1px 4px, #888 4px);
  }
  .front-band {
    position: absolute; left: 0; right: 0; top: 200px; bottom: 0;
    background: var(--orange); text-align: center; color: var(--ink);
  }
  .holder-name {
    font-family: "Lobster", cursive; font-size: 40px; line-height: 1;
    margin-top: 26px; text-transform: uppercase; letter-spacing: 0.5px;
  }
  .holder-role { font-size: 19px; font-weight: 400; margin-top: 8px; letter-spacing: 0.3px; }
  .holder-email { font-size: 14px; font-weight: 700; margin-top: 9px; }

  /* back */
  .back-band {
    position: absolute; left: 0; right: 0; top: 0; height: 218px;
    background: var(--orange); color: #ffffff;
  }
  .brand-block {
    position: absolute; left: 0; width: 297px; top: 56px;
    display: flex; flex-direction: column; align-items: center;
  }
  .brand-dot { width: 30px; height: 30px; border-radius: 50%; background: #ffffff; }
  .brand-name {
    font-weight: 700; font-size: 35px; letter-spacing: 1.5px; margin-top: 12px;
    text-transform: uppercase; line-height: 1;
  }
  .brand-tagline {
    font-size: 11px; font-weight: 500; letter-spacing: 1.2px; margin-top: 9px;
    text-transform: uppercase;
  }
  .back-divider {
    position: absolute; left: 297px; top: 25px; width: 1px; height: 168px;
    background: rgba(255,255,255,0.7);
  }
  .offer {
    position: absolute; left: 323px; top: 30px; width: 260px;
  }
  .offer-headline {
    font-weight: 700; font-size: 18px; line-height: 21px; text-transform: uppercase;
  }
  .offer-body { font-size: 15px; line-height: 19px; margin-top: 7px; }
  .offer-link { font-weight: 700; font-size: 18px; margin-top: 8px; }
  .note-line {
    position: absolute; left: 36px; right: 45px; height: 1px; background: #333;
  }
  .note-line-1 { top: 260px; }
  .note-line-2 { top: 300px; }
</style>
</head>
<body>
  <section class="card card-front">
    <div class="front-mark">
      <div class="mark-circle"></div>
      <div class="mark-name">Lanternfield</div>
    </div>
    <div class="front-rule"></div>
    <div class="front-band">
      <p class="holder-name">Reid Calloway</p>
      <p class="holder-role">STORY MARKETING COACH</p>
      <p class="holder-email">reid@lanternfieldnow.com</p>
    </div>
  </section>

  <section class="card card-back">
    <div class="back-band">
      <div class="brand-block">
        <div class="brand-dot"></div>
        <p class="brand-name">Lanternfield</p>
        <p class="brand-tagline">Tell stories that inspire action</p>
      </div>
      <div class="back-divider"></div>
      <div class="offer">
        <p class="offer-headline">Reach more people.<br>Make more money.<br>Create more impact.</p>
        <p class="offer-body">Get your free Lanternfield Starter Package and our marketing guide today at</p>
        <p class="offer-link">Lanternfieldnow.com/start</p>
      </div>
    </div>
    <div class="note-line note-line-1"></div>
    <div class="note-line note-line-2"></div>
  </section>
</body>
</html>
```